PupCUP Coffee Cup Design

I am looking for a design to be printed on my custom "pup cup" take out cups. These cups will be paper to go cups on the small size, only about 4-6oz not a full size coffee mug. I would like to have an image of our dog with a speech bubble of some sort saying "Hi, I'm Bramble, enjoy your pup cup!" Perhaps a subtle pattern with dog treats or something.
'
I have attached:
1. a picture of a coffee cup along the lines of what I am thinking.
2. My logo which I would like incorporated into the design.
3. Picture of my dog for the inspiration. I would like the design to not have his collar and leash but a bowtie instead. He is a Red Doberman Pinscher. It doesn’t have to be this exact image or pose of him but it is attached her for inspiration. I’m open to artistic freedom to use his image however you see fit.
Target Market(s)
Animal lovers and owners
Industry/Entity Type
Food and beverage, Coffee
Requirements
Must have
- My dog, the provided text, my logo

```html
<!DOCTYPE html>
<html lang="en">
<head>
<meta charset="utf-8">
<title>Pup Cup Wrap – Brew &amp; Bark Depot</title>
<link rel="stylesheet" href="https://fonts.googleapis.com/css2?family=Open+Sans:wght@400&family=Rye&display=swap">
<style>
  :root {
    --paper: #ffffff;
    --visible: #0b5a80;
    --bleed: #e5194f;
    --help: #6f6866;
    --ink: #111111;
    --bubble-dark: #221a17;
    --bubble-mid: #4a4644;
    --bubble-rim: #ffffff;
    --dog-light: #a9784f;
    --dog-mid: #7a5136;
    --dog-dark: #3b2a20;
  }
  * { margin: 0; padding: 0; box-sizing: border-box; }
  html, body {
    width: 1200px; height: 694px; overflow: hidden;
    background: var(--paper);
  }
  .cup-wrap {
    position: relative;
    width: 1200px; height: 694px;
    background: var(--paper);
    font-family: "Open Sans", Arial, sans-serif;
  }
  .legend {
    position: absolute; left: 160px; top: 26px;
    list-style: none;
    font-size: 23px; line-height: 32px;
  }
  .legend__visible { color: var(--visible); }
  .legend__bleed { color: var(--bleed); }
  .legend__help { color: var(--help); }

  .brand-name {
    position: absolute; left: 144px; top: 318px; width: 290px;
    text-align: center;
    font-family: "Rye", Georgia, serif;
    font-size: 36px; line-height: 44px;
    color: var(--ink);
  }

  .mascot-art {
    position: absolute; left: 476px; top: 206px;
    width: 210px; height: 366px;
    border-radius: 48% 48% 10% 10% / 30% 30% 4% 4%;
    background: linear-gradient(180deg, var(--dog-dark) 0%, var(--dog-mid) 35%, var(--dog-light) 75%, var(--dog-mid) 100%);
  }

  .layer { position: absolute; left: 0; top: 0; }
  .speech-bubble__text {
    font-family: "Rye", Georgia, serif;
    font-size: 27px; fill: #ffffff;
    text-anchor: middle;
  }
</style>
</head>
<body>
<main class="cup-wrap">
  <ul class="legend">
    <li class="legend__visible">Visible area</li>
    <li class="legend__bleed">Bleed limit</li>
    <li class="legend__help">Help lines</li>
  </ul>

  <p class="brand-name">Brew &amp; Bark<br>Depot</p>

  <div class="mascot-art" role="img" aria-label="Illustration of Bramble, a red Doberman Pinscher wearing a black bow tie"></div>

  <svg class="layer speech-bubble" width="1200" height="694" viewBox="0 0 1200 694" aria-label="Speech bubble">
    <defs>
      <radialGradient id="bubbleFill" cx="0.55" cy="0.55" r="0.6">
        <stop offset="0" stop-color="var(--bubble-mid)"/>
        <stop offset="1" stop-color="var(--bubble-dark)"/>
      </radialGradient>
      <filter id="bubbleShadow" x="-10%" y="-10%" width="130%" height="140%">
        <feDropShadow dx="4" dy="6" stdDeviation="4" flood-color="#000" flood-opacity="0.35"/>
      </filter>
    </defs>
    <path filter="url(#bubbleShadow)" fill="url(#bubbleFill)" stroke="var(--bubble-rim)" stroke-width="5" stroke-linejoin="round"
      d="M750 276 Q880 262 1018 290 Q1036 296 1033 316 L1022 425 Q1019 440 1004 440 L934 438
         Q925 460 904 472 Q915 455 913 440 Q840 442 770 456 Q755 458 752 442 L736 296 Q735 278 750 276 Z"/>
    <text class="speech-bubble__text" x="883" y="331">HI, I'M BRAMBLE.</text>
    <text class="speech-bubble__text" x="883" y="372">ENJOY YOUR</text>
    <text class="speech-bubble__text" x="883" y="413">PUP CUP!</text>
  </svg>

  <svg class="layer print-guides" width="1200" height="694" viewBox="0 0 1200 694" fill="none" stroke-width="2" aria-hidden="true">
    <g class="print-guides__bleed" stroke="var(--bleed)">
      <rect x="88.5" y="162" width="1020.5" height="403"/>
      <path d="M34 266 Q602 65 1170 252 L1040 633 Q602 488 165 647 Z"/>
    </g>
    <g class="print-guides__visible" stroke="var(--visible)">
      <rect x="100" y="188" width="999" height="365"/>
      <path d="M51 287 Q602 96 1152 273 L1035 619 Q602 479 170 632 Z"/>
    </g>
  </svg>
</main>
</body>
</html>
```